Build Steady Practice Growth Through Trust

Design a cover for this book which is designed to help a business go from it's current revenue and treatment acceptance to double (2X) that success and those metrics.

```html
<!DOCTYPE html>
<html lang="en">
<head>
<meta charset="utf-8">
<title>Build Steady Practice Growth Through Trust</title>
<link rel="stylesheet" href="https://fonts.googleapis.com/css2?family=Montserrat:wght@600&family=Fira+Sans+Extra+Condensed:wght@700&family=Merriweather:wght@700&display=swap">
<style>
  :root {
    --navy-top: #1c374e;
    --navy-bottom: #05325f;
    --band: #003263;
    --title: #ffffff;
    --subtitle: #e1e3e8;
    --bar-grey: #cccccc;
    --bar-orange: #ffa300;
    --bar-teal: #008080;
    --bar-white: #ffffff;
    --grid: #7d8da1;
    --node: #6b7f96;
  }
  * { margin: 0; padding: 0; box-sizing: border-box; }
  html, body { width: 848px; height: 1200px; overflow: hidden; }
  body { background: var(--navy-bottom); }
  .cover {
    position: relative;
    width: 848px;
    height: 1200px;
    overflow: hidden;
    background: linear-gradient(180deg, var(--navy-top) 0%, var(--navy-bottom) 90%);
  }
  .cover-art { position: absolute; inset: 0; }
  .title {
    position: absolute;
    top: 34px;
    left: 0;
    width: 100%;
    text-align: center;
  }
  .title-main {
    display: block;
    font-family: "Montserrat", sans-serif;
    font-weight: 600;
    font-size: 64px;
    line-height: 1.1;
    letter-spacing: -1px;
    color: var(--title);
  }
  .title-sub {
    display: block;
    margin-top: 12px;
    font-family: "Fira Sans Extra Condensed", sans-serif;
    font-weight: 700;
    font-size: 62px;
    line-height: 1;
    letter-spacing: 5px;
    color: var(--subtitle);
  }
  .author-band {
    position: absolute;
    left: 0;
    top: 1077px;
    width: 100%;
    height: 123px;
    background: var(--band);
    border-top: 2px solid var(--bar-grey);
  }
  .author {
    position: absolute;
    left: 0;
    top: 1106px;
    width: 100%;
    text-align: center;
    font-family: "Merriweather", serif;
    font-weight: 700;
    font-size: 42px;
    color: var(--title);
  }
</style>
</head>
<body>
<main class="cover">
  <svg class="cover-art" width="848" height="1200" viewBox="0 0 848 1200" xmlns="http://www.w3.org/2000/svg">
    <defs>
      <linearGradient id="motif-fill" x1="0" y1="0" x2="0" y2="1">
        <stop offset="0" stop-color="#2a4560" stop-opacity="0"/>
        <stop offset="0.5" stop-color="#2a4560" stop-opacity="0.3"/>
        <stop offset="1" stop-color="#0d3560" stop-opacity="0"/>
      </linearGradient>
    </defs>

    <rect class="tooth-motif" x="0" y="230" width="848" height="340" fill="url(#motif-fill)" role="img" aria-label="Illustration of outlined molar teeth with a highlighted white tooth and flowing wave lines"/>

    <g class="grid-lines" stroke="var(--grid)" stroke-width="1.2" fill="none">
      <line x1="40" y1="430" x2="848" y2="430"/>
      <line x1="300" y1="560" x2="848" y2="560"/>
      <line x1="152" y1="560" x2="152" y2="1077"/>
      <line x1="254" y1="760" x2="254" y2="847"/>
      <line x1="597" y1="560" x2="597" y2="627"/>
      <line x1="699" y1="430" x2="699" y2="1077"/>
      <line x1="803" y1="430" x2="803" y2="477"/>
    </g>

    <g class="data-nodes">
      <circle cx="254" cy="760" r="22" fill="none" stroke="var(--grid)" stroke-width="1.2"/>
      <circle cx="254" cy="760" r="5" fill="var(--node)"/>
      <circle cx="597" cy="560" r="22" fill="none" stroke="var(--grid)" stroke-width="1.2"/>
      <circle cx="597" cy="560" r="5" fill="var(--node)"/>
      <circle cx="803" cy="430" r="22" fill="none" stroke="var(--grid)" stroke-width="1.2"/>
      <circle cx="803" cy="430" r="5" fill="var(--node)"/>
    </g>

    <g class="bar-chart">
      <rect x="24" y="917" width="50" height="160" fill="var(--bar-teal)"/>
      <rect x="92" y="877" width="50" height="200" fill="var(--bar-grey)"/>
      <rect x="161" y="827" width="50" height="250" fill="var(--bar-grey)"/>
      <rect x="229" y="847" width="50" height="230" fill="var(--bar-orange)"/>
      <rect x="298" y="777" width="50" height="300" fill="var(--bar-teal)"/>
      <rect x="366" y="737" width="50" height="340" fill="var(--bar-grey)"/>
      <rect x="435" y="757" width="50" height="320" fill="var(--bar-white)"/>
      <rect x="503" y="677" width="50" height="400" fill="var(--bar-grey)"/>
      <rect x="572" y="627" width="50" height="450" fill="var(--bar-teal)"/>
      <rect x="640" y="647" width="50" height="430" fill="var(--bar-orange)"/>
      <rect x="709" y="557" width="50" height="520" fill="var(--bar-grey)"/>
      <rect x="778" y="477" width="50" height="600" fill="var(--bar-teal)"/>
    </g>
  </svg>

  <h1 class="title">
    <span class="title-main">Build Steady Practice</span>
    <span class="title-sub">GROWTH THROUGH TRUST</span>
  </h1>

  <div class="author-band"></div>
  <p class="author">Daniel R. Prescott, DDS</p>
</main>
</body>
</html>
```